Professional Letterhead for electronic use

I would like to inquire, if you could help me to create a letterhead, mostly for electronic use. Preferably in word file, with fixed letterhead design (header and footer), but will allow to add text on the main body of the letter. I usually operate online and would like to be able to add text, convert it to PDF and send as an attachment.
Target Market(s)
High net worth clients.
Industry/Entity Type
Real Estate Agent
Font styles to use
Other font styles liked:
- Century Gothic
Requirements
Must have
- Company name, logo, full address, email address, landline number, website address, Homestead Adjudicator logo, PELV logo, Company registration number
Nice to have
- Professional and elegant design

```html
<!DOCTYPE html>
<html lang="en">
<head>
<meta charset="utf-8">
<title>Corvane Estate Agents – Letterhead</title>
<link rel="stylesheet" href="https://fonts.googleapis.com/css2?family=Questrial&display=swap">
<style>
  :root {
    --backdrop: #ececec;
    --paper: #ffffff;
    --plum: #4a0f36;
    --orange: #e8582a;
    --ink: #3a2a33;
    --watermark: #f3f3f3;
    --badge: #4a0f36;
  }
  * { margin: 0; padding: 0; box-sizing: border-box; }
  html, body {
    width: 1200px;
    height: 898px;
    overflow: hidden;
    background: var(--backdrop);
    font-family: "Questrial", "Century Gothic", sans-serif;
  }
  .letterhead {
    position: absolute;
    left: 303px;
    top: 29px;
    width: 594px;
    height: 840px;
    background: var(--paper);
    box-shadow: 0 4px 18px rgba(0,0,0,0.08);
    overflow: hidden;
  }
  .brand {
    position: absolute;
    left: 48px;
    top: 52px;
    display: flex;
    align-items: center;
    gap: 14px;
  }
  .brand-dot {
    width: 46px;
    height: 46px;
    border-radius: 50%;
    background: var(--orange);
  }
  .brand-name {
    font-size: 22px;
    letter-spacing: 5px;
    color: var(--plum);
    line-height: 1;
  }
  .brand-tagline {
    margin-top: 7px;
    font-size: 8.5px;
    letter-spacing: 3.2px;
    color: var(--orange);
  }
  .watermark {
    position: absolute;
    left: 112px;
    top: 215px;
    width: 370px;
    height: 370px;
  }
  .accreditations {
    position: absolute;
    right: 44px;
    bottom: 46px;
    display: flex;
    align-items: flex-end;
    gap: 18px;
  }
  .badge-adjudicator {
    width: 52px;
    height: 18px;
    background: var(--badge);
  }
  .badge-pelv {
    width: 34px;
    height: 34px;
    border-radius: 50%;
    background: var(--badge);
  }
  .contact {
    position: absolute;
    left: 48px;
    bottom: 36px;
    font-size: 7px;
    line-height: 1.55;
    letter-spacing: 0.6px;
    color: var(--ink);
  }
  .contact .accent { color: var(--orange); }
  .footer-band {
    position: absolute;
    left: 0;
    right: 0;
    bottom: 0;
    height: 22px;
    background: var(--plum);
    display: flex;
    align-items: center;
    justify-content: center;
  }
  .website {
    font-size: 7.5px;
    letter-spacing: 1.6px;
    color: var(--orange);
  }
</style>
</head>
<body>
  <main class="letterhead">
    <header class="brand">
      <span class="brand-dot"></span>
      <div class="brand-text">
        <div class="brand-name">CORVANE</div>
        <div class="brand-tagline">ESTATE AGENTS</div>
      </div>
    </header>

    <svg class="watermark" viewBox="0 0 100 100" aria-hidden="true">
      <circle cx="50" cy="50" r="50" fill="var(--watermark)"/>
    </svg>

    <div class="accreditations">
      <span class="badge-adjudicator" role="img" aria-label="Homestead Adjudicator membership badge"></span>
      <span class="badge-pelv" role="img" aria-label="PELV membership badge"></span>
    </div>

    <footer>
      <address class="contact">
        <div class="accent">42 Elmwood Lane, Belsize, London, NW9 4QT</div>
        <div>Sales Telephone <span class="accent">02071846320</span> Lettings Telephone <span class="accent">02071846395</span> Reg No. <span class="accent">07315548</span></div>
      </address>
      <div class="footer-band">
        <span class="website">www.corvane.co.uk</span>
      </div>
    </footer>
  </main>
</body>
</html>
```